TR Hornets Dunmore (Social Media Pack & Stationary)

Create Stationary Designs as well as Social Media Designs (Twitter, Instagram & Facebook) as well as a Square and Banner Social media template... keep the logo I attached in the Ai file... I would like the blue in the TR Hornets logo to be navy blue instead of the dark blue.

Willing to give a good tip to get it done quicker

Please use the logo provided in the ai file.

Instagram account: @trhdunmore
FB account: TR Hornets Dunmore
Twitter: @trhdunmore

Target Market(s)

Parents and players

Font styles to use
Serif

Colors
0255a3
f78f20
f37122

Requirements
Must have
• Stationary
Twitter & FB heading
Template to post social media announcements
Template for pictures to post on social media
Template to post schedule
Envelop
Business Card
(All must include logo)

```html
<!DOCTYPE html>
<html lang="en">
<head>
<meta charset="utf-8">
<title>TR Hornets Dunmore — Stationery</title>
<link href="https://fonts.googleapis.com/css2?family=Karla:wght@400;700;800&display=swap" rel="stylesheet">
<style>
  :root {
    --backdrop: #e6e6e6;
    --paper: #f5f5f5;
    --orange: #e95d3b;
    --navy: #2b2f8f;
    --ink: #2a2a2a;
    --pattern: #ef7a5c;
  }
  * { margin: 0; padding: 0; box-sizing: border-box; }
  html, body { width: 1200px; height: 1000px; overflow: hidden; }
  body {
    position: relative;
    background: var(--backdrop);
    font-family: "Karla", Arial, sans-serif;
    color: var(--ink);
  }
  .sheet { position: absolute; background: var(--paper); }

  .wordmark {
    position: absolute;
    display: flex;
    flex-direction: column;
    align-items: flex-end;
    color: var(--orange);
    font-weight: 800;
    line-height: 0.95;
    letter-spacing: -0.02em;
    white-space: nowrap;
  }
  .wordmark .wordmark-place { font-size: 0.38em; }
  .wordmark .wordmark-name { font-size: 1em; }

  /* Business card front */
  .card-front { left: 507px; top: 127px; width: 188px; height: 105px; }
  .card-front .wordmark { font-size: 27px; left: 50%; top: 32px; transform: translateX(-50%); }

  /* Business card back */
  .card-back { left: 738px; top: 128px; width: 186px; height: 107px; }
  .card-back .card-band {
    position: absolute; left: 0; top: 0; width: 100%; height: 77px;
    background: var(--orange);
    display: flex; flex-direction: column; align-items: center; justify-content: center;
    color: #fff; font-size: 7.5px; font-weight: 700; line-height: 1.3; letter-spacing: 0.04em;
    text-transform: uppercase;
  }
  .card-back .wordmark { font-size: 13px; left: 50%; top: 83px; transform: translateX(-50%); }

  /* Letterhead */
  .letterhead { left: 508px; top: 275px; width: 450px; height: 583px; }
  .letterhead .wordmark { font-size: 32px; right: 30px; top: 40px; }
  .letter-body {
    position: absolute; left: 72px; top: 270px; width: 346px;
    font-size: 9px; line-height: 15.5px;
  }
  .letter-footer {
    position: absolute; left: 0; bottom: 0; width: 100%; height: 32px;
    background: linear-gradient(90deg, var(--orange) 0%, #b04a5a 30%, #5a2e8a 55%, var(--navy) 75%);
  }

  /* Envelope back */
  .envelope-back { left: 113px; top: 378px; width: 455px; height: 187px; }
  .envelope-back .wordmark { font-size: 32px; left: 50%; top: 70px; transform: translateX(-50%); }

  /* Envelope front */
  .envelope-front { left: 105px; top: 597px; width: 465px; height: 197px; overflow: hidden; }
  .envelope-front .envelope-colour {
    position: absolute; left: 0; top: 0; width: 100%; height: 116px; background: var(--orange);
  }
  .envelope-front .envelope-flap { position: absolute; left: 0; top: 0; }
  .envelope-front .wordmark { font-size: 29px; right: 14px; top: 138px; }
</style>
</head>
<body>

  <div class="sheet card-front">
    <div class="wordmark"><span class="wordmark-place">Dunmore</span><span class="wordmark-name">TR Hornets</span></div>
  </div>

  <div class="sheet card-back">
    <div class="card-band">
      <span>Dana Reyes</span>
      <span>dana.r@trhornets.com</span>
      <span>+800 555 12 34</span>
    </div>
    <div class="wordmark"><span class="wordmark-place">Dunmore</span><span class="wordmark-name">TR Hornets</span></div>
  </div>

  <div class="sheet letterhead">
    <div class="wordmark"><span class="wordmark-place">Dunmore</span><span class="wordmark-name">TR Hornets</span></div>
    <p class="letter-body">Lorem ipsum dolor sit amet, consectetur adipiscing elit. Cras at tempus diam. Aliquam urna tortor, convallis in justo eu, tempor porttitor nunc. Aliquam lacinia nisi malesuada, blandit ligula facilisis, iaculis dolor. Cras vel vehicula massa. Etiam posuere convallis dignissim. Etiam at quam ornare, mattis eros ut, blandit mi. In sit amet sapien eget odio eleifend hendrerit sed eu velit. Fusce eu felis ac erat blandit ullamcorper.</p>
    <div class="letter-footer"></div>
  </div>

  <div class="sheet envelope-back">
    <div class="wordmark"><span class="wordmark-place">Dunmore</span><span class="wordmark-name">TR Hornets</span></div>
  </div>

  <div class="sheet envelope-front">
    <div class="envelope-colour"></div>
    <svg class="envelope-flap" width="465" height="64" viewBox="0 0 465 64" role="img" aria-label="Envelope flap with a fine orange check pattern">
      <path d="M0 0 H465 V30 Q465 40 455 44 L448 48 Q440 62 425 62 H25 Q12 62 10 50 L8 44 Q0 40 0 30 Z" fill="var(--pattern)"/>
    </svg>
    <div class="wordmark"><span class="wordmark-place">Dunmore</span><span class="wordmark-name">TR Hornets</span></div>
  </div>

</body>
</html>
```